High End Business Card Design for Flooring Store

Looking for a new card design for our hardwood flooring company. We have no print budget for these and are open to cards made from wood, metal, cardstock with embossed print ... or any combination of these. No plastic.

We sell luxury products and I want the cards to reflect our image of quality and class.

Our contact information as such;
Employee Name
248 Halloway Blvd.
Dieppe, NB
E3C-4K9
(506) 555-0142
Employee email @kestraflooring.com

Target Market(s)

Home Builders

Contact Information for Business Card

Emnployee name, business contact information

```html
<!DOCTYPE html>
<html lang="en">
<head>
<meta charset="utf-8">
<title>Kestra Flooring – Business Card</title>
<link rel="stylesheet" href="https://fonts.googleapis.com/css2?family=Montserrat:wght@400;500;700&display=swap">
<style>
  :root {
    --brand-red: #922a25;
    --brand-gold: #e8b226;
    --ink: #3a2b2b;
    --card-white: #ffffff;
    --card-grey: #6d6d6d;
    --emboss-grey: #5a5a5a;
    --emboss-light: #8a8a8a;
    --page-bg: #e9e6e2;
  }
  * { box-sizing: border-box; margin: 0; padding: 0; }
  html, body {
    width: 1200px; height: 900px; overflow: hidden;
    background: var(--page-bg);
    font-family: "Montserrat", Arial, sans-serif;
  }
  .canvas {
    width: 1200px; height: 900px;
    display: flex; flex-direction: column;
    align-items: center; justify-content: center; gap: 36px;
  }
  .card {
    position: relative;
    width: 700px; height: 400px;
    overflow: hidden;
    box-shadow: 0 4px 14px rgba(0,0,0,0.18);
  }

  /* Back side */
  .card-back {
    background: var(--card-grey);
    display: flex; align-items: center; justify-content: center;
  }
  .back-mark { display: flex; align-items: center; gap: 22px; }
  .back-square { width: 70px; height: 70px; background: var(--emboss-light); }
  .back-text { display: flex; flex-direction: column; }
  .back-name {
    font-weight: 500; font-size: 104px; line-height: 0.95;
    color: var(--emboss-grey); letter-spacing: -1px;
  }
  .back-tagline {
    font-weight: 500; font-size: 24px; line-height: 1.15;
    color: var(--emboss-grey); margin-left: 8px;
  }

  /* Front side */
  .card-front { background: var(--card-white); }
  .front-wave { position: absolute; inset: 0; }
  .name-bar {
    position: absolute; left: 26px; top: 97px;
    width: 10px; height: 68px; background: var(--brand-gold);
  }
  .identity { position: absolute; left: 50px; top: 95px; }
  .employee-name {
    font-weight: 700; font-size: 36px; line-height: 1.1; color: var(--brand-gold);
  }
  .employee-name .last { color: var(--brand-red); }
  .employee-title {
    font-weight: 400; font-size: 20px; color: var(--ink); margin-top: 4px;
  }
  .contacts {
    position: absolute; left: 70px; top: 180px;
    list-style: none; font-size: 19px; color: var(--ink); line-height: 1.5;
  }
  .contacts li { display: flex; align-items: center; gap: 10px; }
  .contacts svg { width: 18px; height: 18px; fill: var(--brand-red); flex: none; }
  .address {
    position: absolute; left: 98px; top: 245px;
    font-style: normal; font-size: 20px; line-height: 1.35; color: var(--ink);
  }
  .front-mark {
    position: absolute; right: 40px; top: 30px;
    display: flex; align-items: flex-start; gap: 12px;
  }
  .front-square {
    width: 40px; height: 40px; background: var(--brand-gold); margin-top: 14px;
  }
  .front-name {
    font-weight: 500; font-size: 62px; line-height: 1; color: var(--brand-red);
  }
  .front-tagline {
    font-weight: 500; font-size: 14px; line-height: 1.2; color: var(--ink);
    margin-left: 30px; margin-top: 2px;
  }
  .website {
    position: absolute; right: 36px; bottom: 28px;
    font-size: 18px; color: var(--card-white);
  }
</style>
</head>
<body>
<main class="canvas">

  <section class="card card-back" aria-label="Card back">
    <div class="back-mark">
      <div class="back-square"></div>
      <div class="back-text">
        <span class="back-name">Kestra</span>
        <span class="back-tagline">Planchers &amp; Escaliers<br>Flooring &amp; Stairs</span>
      </div>
    </div>
  </section>

  <section class="card card-front" aria-label="Card front">
    <svg class="front-wave" viewBox="0 0 700 400" preserveAspectRatio="none" aria-hidden="true">
      <path d="M0,350 C260,358 450,300 590,215 C460,295 260,368 0,372 Z" fill="var(--brand-gold)"/>
      <path d="M0,378 C300,378 520,260 700,140 L700,400 L0,400 Z" fill="var(--brand-red)"/>
    </svg>

    <div class="front-mark">
      <div class="front-square"></div>
      <div>
        <div class="front-name">Kestra</div>
        <div class="front-tagline">Planchers &amp; Escaliers<br>Flooring &amp; Stairs</div>
      </div>
    </div>

    <div class="name-bar"></div>
    <div class="identity">
      <h1 class="employee-name">Employee <span class="last">Name</span></h1>
      <p class="employee-title">Owner/CEO</p>
    </div>

    <ul class="contacts">
      <li>
        <svg viewBox="0 0 24 24" aria-hidden="true"><path d="M6.6 10.8a15.1 15.1 0 0 0 6.6 6.6l2.2-2.2a1 1 0 0 1 1-.25 11.4 11.4 0 0 0 3.6.57 1 1 0 0 1 1 1V20a1 1 0 0 1-1 1A17 17 0 0 1 3 4a1 1 0 0 1 1-1h3.5a1 1 0 0 1 1 1c0 1.25.2 2.45.57 3.57a1 1 0 0 1-.25 1z"/></svg>
        (506) 555-0142
      </li>
      <li>
        <svg viewBox="0 0 24 24" aria-hidden="true"><path d="M3 5h18a1 1 0 0 1 1 1v12a1 1 0 0 1-1 1H3a1 1 0 0 1-1-1V6a1 1 0 0 1 1-1zm1 2.3V17h16V7.3l-8 5.2z M5.2 7 12 11.4 18.8 7z"/></svg>
        info@kestraflooring.com
      </li>
    </ul>

    <address class="address">248 Halloway Blvd.<br>Dieppe, NB E3C-4K9</address>

    <p class="website">www.kestraflooring.com</p>
  </section>

</main>
</body>
</html>
```